start up personal training business needs logo and business cards

need a logo and a design for business cards
the business is named ROK fitness

Industry/Entity Type

Training

```html
<!DOCTYPE html>
<html lang="en">
<head>
<meta charset="utf-8">
<title>rok fitness – Logo and Business Cards</title>
<link rel="stylesheet" href="https://fonts.googleapis.com/css2?family=Questrial&display=swap">
<style>
  :root {
    --backdrop: #d9d5d5;
    --card-black: #060606;
    --brand-orange: #e57a2f;
    --ghost: #1a1818;
    --text-light: #e9e9e9;
    --rule: #7a7a7a;
    --white: #ffffff;
  }
  * { box-sizing: border-box; margin: 0; padding: 0; }
  html, body { width: 1200px; height: 845px; overflow: hidden; }
  body {
    background: var(--backdrop);
    font-family: "Questrial", "Century Gothic", sans-serif;
    position: relative;
  }
  .card {
    position: absolute;
    width: 500px;
    height: 286px;
    background: var(--card-black);
    overflow: hidden;
    box-shadow: 0 6px 16px rgba(0,0,0,.25);
  }
  .card--back { left: 70px; top: 80px; }
  .card--front { left: 630px; top: 80px; }

  .ghost-mark {
    position: absolute;
    left: 0;
    right: 0;
    text-align: center;
    color: var(--ghost);
    font-size: 64px;
    line-height: 1;
    white-space: nowrap;
    letter-spacing: 1px;
  }
  .card--back .ghost-mark { top: 160px; }

  .wordmark {
    position: absolute;
    color: var(--brand-orange);
    white-space: nowrap;
    line-height: 1;
    letter-spacing: 0.5px;
  }
  .card--back .wordmark { left: 0; right: 0; top: 90px; text-align: center; font-size: 34px; }
  .card--front .wordmark { left: 40px; top: 52px; font-size: 26px; }

  .holder {
    position: absolute;
    right: 36px;
    top: 40px;
    text-align: right;
  }
  .holder__name {
    color: var(--white);
    font-size: 22px;
    padding-bottom: 4px;
    border-bottom: 1px solid var(--text-light);
  }
  .holder__role {
    color: var(--brand-orange);
    font-size: 12px;
    margin-top: 4px;
  }

  .divider {
    position: absolute;
    left: 40px;
    right: 40px;
    top: 140px;
    border-top: 1px solid var(--rule);
  }

  .contact {
    position: absolute;
    left: 40px;
    top: 156px;
    display: grid;
    grid-template-columns: 64px 1fr;
    row-gap: 5px;
    color: var(--text-light);
    font-size: 12px;
    line-height: 1.3;
  }
  .contact dd::before { content: ": "; }

  .card__band { position: absolute; left: 0; top: 0; }
  .band__url {
    font-family: "Questrial", "Century Gothic", sans-serif;
    font-size: 14px;
    fill: var(--white);
  }

  .logo-standalone {
    position: absolute;
    right: 90px;
    bottom: 110px;
    color: var(--brand-orange);
    font-size: 64px;
    line-height: 1;
    white-space: nowrap;
    letter-spacing: 1px;
  }
</style>
</head>
<body>

  <section class="card card--back" aria-label="Business card, logo side">
    <div class="ghost-mark" aria-hidden="true">rok fitness</div>
    <div class="wordmark">rok fitness</div>
  </section>

  <section class="card card--front" aria-label="Business card, contact side">
    <div class="wordmark">rok fitness</div>

    <div class="holder">
      <p class="holder__name">Sam Carter</p>
      <p class="holder__role">Managing Director</p>
    </div>

    <div class="divider"></div>

    <dl class="contact">
      <dt>Phone</dt><dd>13 58 20</dd>
      <dt>Adress</dt><dd>Suite 14, 9-11 Lakeview Road, Riverton VIC 3900,<br>Melbourne</dd>
      <dt>Email</dt><dd>samcarter@rokfitness.com</dd>
    </dl>

    <svg class="card__band" width="500" height="286" viewBox="0 0 500 286" aria-hidden="true">
      <polygon points="90,286 318,246 330,246 300,286" fill="var(--white)"/>
      <polygon points="300,286 332,240 500,240 500,286" fill="var(--brand-orange)"/>
      <text class="band__url" x="478" y="268" text-anchor="end">www.rokfitness.com</text>
    </svg>
  </section>

  <div class="logo-standalone" aria-label="rok fitness logo">rok fitness</div>

</body>
</html>
```